Etikettendesign für Imkereiprodukt
Zielgruppe
Ich betreibe eine Imkerei nach ökologischen Gesichtspunkten und vertreibe alles rund um die Biene- Honig, Wachs, Met, Likör...
Aus Bienenwachs und reinem Leinöl stelle ich ein natürliches Holzwachs her. (Wachs stammt aus eigener Bio Imkerei, Leinöl wird in Deutschland hergestellt)
Mit dem Wachs werden unbehandelte Hölzer imprägniert, gegen Feuchtigkeit geschützt, das Wachs verleiht dem Holz einen matten Glanz
Für dieses Produkt benötige ich ein Etikett.
Aufgabenstellung
- rundes Etikett Durchmesser 85 mm
- Verwendung von eigenem Firmenlogo (Anhang) (Name der Imkerei auch 'Wabenritter')
- Verwendung von folgenden Textbausteinen:
'ausschließlich Leinöl und Bienenwachs'
'regional von Hand hergestellt'
'komplett ohne Lösungsmittel'
oder ähnlich
- Herstelleradresse
- Datei nach Druck-vorgaben

```html
<!DOCTYPE html>
<html lang="de">
<head>
<meta charset="utf-8">
<title>Wabenritter Holzwachs – Etikett</title>
<link rel="stylesheet" href="https://fonts.googleapis.com/css2?family=Uncial+Antiqua&family=Source+Sans+3:wght@400&family=Roboto+Condensed:wght@400;700&display=swap">
<style>
  :root {
    --page: #efefef;
    --label-cream: #e9ddbd;
    --gold: #c4a259;
    --gold-dark: #7a5f2c;
    --brown: #4a2d1a;
    --ink: #4f3a25;
    --white: #ffffff;
  }
  html, body {
    margin: 0;
    padding: 0;
    width: 1114px;
    height: 1200px;
    overflow: hidden;
    background: var(--page);
  }
  .label { display: block; width: 1114px; height: 1200px; }
  .label__brand { font-family: "Uncial Antiqua", serif; fill: var(--gold); font-size: 46px; }
  .label__title { font-family: "Uncial Antiqua", serif; fill: var(--gold); font-size: 124px; }
  .label__claim { font-family: "Source Sans 3", sans-serif; fill: var(--ink); font-size: 28px; }
  .label__maker { font-family: "Roboto Condensed", sans-serif; fill: var(--white); font-size: 27px; font-weight: 700; }
  .label__address { font-family: "Roboto Condensed", sans-serif; fill: var(--white); font-size: 27px; font-weight: 400; }
</style>
</head>
<body>
<svg class="label" viewBox="0 0 1114 1200" xmlns="http://www.w3.org/2000/svg">
  <defs>
    <clipPath id="label-shape">
      <circle cx="557" cy="600" r="520"/>
    </clipPath>
  </defs>

  <g clip-path="url(#label-shape)">
    <rect class="label__field" x="0" y="0" width="1114" height="1200" fill="var(--label-cream)"/>
    <rect class="label__footer-band" x="0" y="878" width="1114" height="330" fill="var(--brown)"/>
  </g>

  <circle class="label__ring" cx="557" cy="600" r="500" fill="none" stroke="var(--white)" stroke-width="3"/>
  <circle class="label__dots" cx="557" cy="600" r="484" fill="none" stroke="var(--gold)"
          stroke-width="8" stroke-linecap="round" stroke-dasharray="0 15.2"/>

  <g class="label__brand-mark">
    <circle cx="557" cy="270" r="80" fill="none" stroke="var(--gold)" stroke-width="6"/>
  </g>

  <text class="label__brand" x="557" y="500" text-anchor="middle">wabenritter</text>
  <text class="label__title" x="557" y="645" text-anchor="middle">holzwachs</text>

  <text class="label__claim" x="557" y="718" text-anchor="middle">natürliches Holzpflegemittel aus Leinöl &amp; Bienenwachs</text>
  <text class="label__claim" x="557" y="756" text-anchor="middle">ohne Lösungsmittel regional von Hand hergestellt</text>

  <text class="label__maker" x="557" y="932" text-anchor="middle">Imkerei Jonas Harbeck</text>
  <text class="label__address" x="557" y="968" text-anchor="middle">Heideweg 7 • 14650 Wiesenau</text>
  <text class="label__address" x="557" y="1003" text-anchor="middle">Tel. +49 160 55501234</text>
</svg>
</body>
</html>
```